Clockharbour Homepage Banner 1060 W x 100 H

Please see the attached 'word' document (Also copied below)
Feel free to use any images or logos from our website.
www.clockharbour.com.au

Background:
We are an Australian based official watch distributor/online retailer of international watch brands.

We require a new banner ad (1060 W x 100 H) to replace the existing one on our homepage www.clockharbour.com.au & wish to convey the following information:
*(Please feel free to alter wording, include or exclude points below & generally take creative license (with commercial reality in mind). We sell some luxury watches, so it must look professional & maintain a luxury look & feel.)

Clockharbour Direct:
Revolutionising the retail watch market !

- Buy direct from the official distributor & get world competitive
online prices (with full international warranty, & all original
papers, box & invoice)

- Eliminate all risk of fakes & non-existent factory warranty from
'grey' market sellers

- Free worldwide delivery over A$300

- Order online & 'try-on' in the comfort of your own home.
If you're not 100% happy, just post it back for a full refund or
exchange within 30 days

- Prefer to see & try on before purchase? Visit one of our retail
partner stores.

*** Feel free to copy any images from our website
www.clockharbour.com.au
Updates

Target Market(s)

Luxury watches

Industry/Entity Type

Retail

Font styles to use
Sans Serif

Requirements
Must have
• Visual imagery, text
Nice to have
• Feel free to use your creativity...
Should not have
• Cheap looking or tacky images. We sell some luxury watches, so we need to keep a professional & luxury image.

```html
<!DOCTYPE html>
<html lang="en">
<head>
<meta charset="utf-8">
<title>Homepage Banner</title>
<link rel="stylesheet" href="https://fonts.googleapis.com/css2?family=Federo&display=swap">
<style>
  :root {
    --navy: #0f1d4d;
    --navy-ring: #1c2f6e;
    --gold-deep: #9c7e48;
    --gold-mid: #b99a62;
    --gold-light: #cdb383;
    --tan-light: #d6bf93;
    --text: #ffffff;
  }
  html, body {
    margin: 0;
    padding: 0;
    width: 1200px;
    height: 113px;
    overflow: hidden;
  }
  .banner {
    position: relative;
    width: 1200px;
    height: 113px;
    overflow: hidden;
    background: linear-gradient(90deg,
      var(--gold-deep) 0%,
      var(--gold-mid) 25%,
      var(--gold-light) 48%,
      var(--gold-mid) 58%,
      var(--gold-light) 80%,
      var(--tan-light) 100%);
    font-family: "Federo", sans-serif;
    color: var(--text);
    text-transform: uppercase;
  }
  .brand-mark {
    position: absolute;
    left: 0;
    top: 0;
    width: 110px;
    height: 113px;
  }
  .message {
    position: absolute;
    top: 0;
    height: 113px;
    margin: 0;
    text-align: center;
    white-space: nowrap;
  }
  .message span {
    position: absolute;
    left: 0;
    right: 0;
    line-height: 20px;
  }
  .message--store { left: 120px; width: 394px; font-size: 15px; }
  .message--home  { left: 535px; width: 616px; font-size: 16px; }
</style>
</head>
<body>
  <div class="banner">
    <svg class="brand-mark" viewBox="0 0 110 113" aria-hidden="true">
      <circle cx="46" cy="57" r="55" fill="var(--navy)" stroke="var(--navy-ring)" stroke-width="3"/>
    </svg>

    <p class="message message--store">
      <span style="top:10px">Buy direct from the official distributor</span>
      <span style="top:33px">and get world competitive online prices</span>
      <span style="top:61px">Visit one of our retail partner stores</span>
      <span style="top:86px">and try it on before purchasing</span>
    </p>

    <p class="message message--home">
      <span style="top:8px">Order online &amp; ‘try-on’ in the comfort of your own home</span>
      <span style="top:40px">If you’re not 100% happy, just post it back for a full refund</span>
      <span style="top:60px">or exchange within 30 days</span>
      <span style="top:88px">Free worldwide delivery over A$300</span>
    </p>
  </div>
</body>
</html>
```